Streak Sparrow App – Elite Performance Sales Page Design (Solo + Team Focus)

We need a high-converting, direct-response style sales page for Streak Sparrow, our business performance system trusted by entrepreneurs, teams, and business leaders.

What we want:

Clean, modern, authority-building design with visual clarity.

Layout should drive action (“Try Now” not “Buy”).

Showcase 8 Elite Business Habits visually (icons or cards), with room for short, punchy benefit bullets.

Solo user and team user appeal throughout—must feel inclusive for both.

Prominent above-the-fold area for hero headline, subhead, call-to-action button, and trust signals (as seen on, testimonials).

Visual section for “How It Works,” “Why Streak Sparrow is Different,” and real testimonials (images provided).

Space for short explainer video.

No mention of guarantee or order bumps on the main sales page—focus on core offer and benefits.

Branding to match “Streak Sparrow” and TopVentureGuide.ca (see uploads for inspiration).

Colors: Blues, orange, white, black—modern, energetic, professional.

Goals:

Drive trial signups for $1/30 days, then $37/month.

Make it easy to see value for both individuals and teams.

Position Streak Sparrow as the only serious alternative to boring apps, with research and results credibility.

----

Project Summary for Designers

What We Do:
Streak Sparrow is a business performance system for both solo entrepreneurs and teams. It’s not just a habit tracker, it’s a research-backed platform guiding users through the 8 Critical Business Habits proven to drive results.

Our system is trusted by business owners, CEOs, coaches, and ambitious individuals who want accountability, results, and measurable growth.

Who We Serve:

Business owners, CEOs, team leaders, coaches, and high-performers (teams or individuals)

Freelancers and solopreneurs ready to level up

People who want real accountability and visible results

What Makes Us Unique:

Built from $50,000+ in research and 555+ expert interviews

Focuses on 8 Critical Business Habits (make this a visual/hero section!)

Used by clients to close $44k in 45 days, build $1M+ companies, and drive massive team engagement

Supports team/group features: leaderboards, group stats, private activity feeds, and easy group facilitation

Proven results, statistically validated (NOT just another productivity app)

Design & Messaging Must-Haves:

Clean, modern, authority-driven design that inspires action

Above-the-fold: clear headline, subhead, social proof, call-to-action button ("Try Streak Sparrow Now")

Integrate the 8 Critical Habits visually (icon cards or graphics)

Make solo users feel included (section or callout: "Works for Teams & Driven Individuals")

Real testimonials (faces + stories provided)

Highlight: 90 Days To 8 Better Biz Habits (“Rewire Your Day For Success in 90 Days”)

“Statistically Proven,” “Research-Backed,” “Built for Survival & Growth—Even in Tough Times”

Visuals for both engaged teams and motivated solo users

Optional section for “How It Works” (52-week journey, gamified, adaptive)

Clear, trust-building, NOT hype or magic pill promises

Avoid any mention of guarantee/order bump (leave to order form)

Copy & Story to Highlight (For Designers)

Attraction: “These 8 Critical Business Habits Decide Who Survives—Master Them in 90 Days”

Engagement: Real-world stories of Owen, Lyle, Dmitri (see testimonials)

Sales: Action-driven, with clear benefits (for you or your team)—see the bullet points and success stories provided

Use authority: “Based on $50,000+ in research, 555+ interviews, and proven by business owners worldwide.”

Pains, Dreams, Desires from User Surveys (Integrate These)

Top Pains:

Lack of accountability, falling off track after initial excitement

Goals set, but habits not sticking—missed deadlines, lost sales

Overwhelm from too many tools, not enough results

“Tired of doing it alone” or seeing teams underperform

Top Dreams/Desires:

Predictable, measurable growth (not just hope)

Having a “secret weapon” that makes habits automatic

Winning team culture (or self-mastery for solo users)

Fast results (“I want to see a difference in 30-90 days”)

A proven system that works—no more guesswork

Biggest Emotional Drivers:

Wanting to be seen as a leader/hero in their business

“Done with busywork—ready for real change”

Desire to finally reach their potential (for self or team)

Design Visuals

Show solo AND team success: group dashboards, solo achievement streaks, celebrations

Easy-to-follow, gamified interface mockups (not busy or cluttered)

Faces: real testimonials, proof, success stories

Authority badges (“As Seen In,” “Trusted by CEOs & Teams,” etc.)

“Try Streak Sparrow Now” button (not “Buy”)

Instruct designers:

Read the attached story & messaging playbook to understand our voice and value.

Use the provided headlines, copy, and testimonials wherever you can.

Design for action, credibility, and clarity. Focus on results, not “features overload.”

Remember: page should sell both solo AND team users—show this visually and in the copy.

Bottom Line:
Our page should feel like the next-level solution for business performance—the only system that works for both teams and individuals who want to finally get results.

---

Proven Copy Headlines:
Rewire Your Day For Success.
8 Business Habits To Survive
These 8 Critical Business Habits Decide Who Survives During Uncertain Times & Who Doesn't
Good Customer Service. Recommended Productivity Challenge.
Develops habits statistically proven to improve results for CEOs, marketing & sales teams.
New Business Coach & Accountability Partner For Business, Fitness & Mindset. All In One.
90 Days To Fix Business Habits
90 Days To 8 Better Biz Habits
8 Critical Habits of Business
The 8 Critical Business Habits

90 Days To 8 Types of Better Business, Fitness & Mindset Habits Or Get 3x Your MoneyBack

Target Market(s)

Entrepreneurs, team leaders, coaches, sales managers, CEOs, and other business leaders who seek measurable growth and want to build and reinforce effective business habits in their teams or individually.

Industry/Entity Type

Business coaching, personal development, team performance, business systems.

Coding

Coded - Design and coding required

Number of Pages Required

1 page

Font styles to use
Sans Serif

Colors

Designer to choose colors to be used in the design.

Requirements
Must have
• Direct-response design: Engaging copy with a focus on driving conversions. Mobile-friendly and optimized for high conversion rates.Visuals showing results from users, especially testimonials and proof points. Sections that clearly differentiate Streak Sparrow’s value for individual users and teams.Social proof and testimonials with photos or video clips from actual users. A clean, professional, and modern design that feels "elite" and exclusive.
Nice to have
• Visual emphasis on the 8 Critical Business Habits (use icons or graphics for each habit).
Should not have
• Overly complex or cluttered layouts. Unnecessary distractions or complex animations. Any complex jargon that could confuse the potential customers.

```html
<!DOCTYPE html>
<html lang="en">
<head>
<meta charset="utf-8">
<title>Streak Sparrow – Rewire Your Day for Success</title>
<link href="https://fonts.googleapis.com/css2?family=Montserrat:wght@400;500;600;700;800&family=Playfair+Display:wght@700&display=swap" rel="stylesheet">
<style>
:root{
  --backdrop:#b2ab9b;
  --orange:#c8590f;
  --orange-bright:#e07a1c;
  --gold:#f2b437;
  --ink:#141414;
  --cream:#fffbec;
  --sand:#f5e6cc;
  --white:#ffffff;
  --grey-dark:#3a3a3a;
  --text:#333333;
}
*{box-sizing:border-box;margin:0;padding:0}
html,body{width:1200px;height:3841px;overflow:hidden}
body{background:var(--backdrop);font-family:"Montserrat",sans-serif;color:var(--ink)}
.page{position:absolute;left:72px;top:80px;width:1056px;background:var(--white);box-shadow:0 6px 24px rgba(0,0,0,.25)}
section{position:relative;overflow:hidden}
.eyebrow{display:flex;align-items:center;justify-content:center;gap:8px;font-size:12px;font-weight:700;letter-spacing:.5px}
.eyebrow::before,.eyebrow::after{content:"";width:34px;height:2px;background:var(--ink)}
.title{text-align:center;font-size:39px;font-weight:400;letter-spacing:.5px;line-height:1.05}
.title b{font-weight:800}

/* hero */
.hero{height:561px}
.hero-art{position:absolute;inset:0;background:radial-gradient(circle at 70% 35%,#ffe08a 0%,#f6a22c 25%,#e07a1c 50%,#c25a10 80%)}
.hero-city{position:absolute;left:0;right:0;bottom:0;height:140px;background:linear-gradient(to top,#7a4a14,rgba(150,90,20,.6) 70%,rgba(0,0,0,0))}
.hero-figures{position:absolute;left:560px;top:70px;width:450px;height:470px;background:radial-gradient(ellipse at 50% 60%,rgba(30,20,10,.85),rgba(30,20,10,.4) 55%,rgba(0,0,0,0) 72%)}
.brand-title{position:absolute;left:98px;top:52px;font-size:53px;line-height:64px;font-weight:800;color:var(--ink)}
.hero-frame{position:absolute;left:52px;top:133px}
.hero-copy{position:absolute;left:96px;top:126px;color:var(--white);width:340px}
.hero-copy .kicker{font-size:12px;line-height:14px;font-weight:700;display:flex;align-items:center;gap:6px}
.hero-copy .kicker::after{content:"";width:34px;height:2px;background:var(--white)}
.hero-copy h1{font-size:40px;font-weight:400;line-height:42px;white-space:nowrap}
.hero-copy h1 b{font-weight:800}
.hero-copy p{font-size:15px;line-height:23px;margin-top:10px;white-space:nowrap}
.hero-cta{position:absolute;left:154px;top:318px;background:var(--ink);color:var(--white);font-size:12px;line-height:14px;font-weight:800;padding:8px 18px 8px 14px;clip-path:polygon(0 0,100% 0,94% 100%,0 100%)}

.nav{height:33px;background:var(--ink);color:var(--white);display:flex;align-items:center;justify-content:space-between;padding:0 12px 0 16px}
.nav .brand{font-weight:700;font-size:15px}
.nav ul{display:flex;gap:25px;list-style:none;font-size:10px;font-weight:500}

/* seen on */
.seen{height:310px;padding-top:52px}
.seen-grid{display:flex;justify-content:center;gap:2px;margin-top:30px}
.seen-card{width:237px;height:146px;background:var(--cream);display:flex;flex-direction:column;align-items:center;justify-content:center;gap:14px;font-size:17px}
.badge{width:40px;height:40px;border:2px solid var(--orange);border-radius:50%}

/* habits */
.habits-head{height:122px;padding-top:40px}
.habits{height:464px;display:grid;grid-template-columns:repeat(4,1fr);gap:2px}
.habit{background:var(--cream);text-align:center;padding-top:38px}
.habit svg{width:76px;height:76px}
.habit h3{font-size:20px;font-weight:600;margin-top:14px}
.habit p{font-size:14px;line-height:1.3;color:var(--text);margin:8px auto 0;width:230px}

/* built for */
.built{height:547px;background:var(--sand);padding-top:60px}
.built .title{font-size:39px;margin-top:6px}
.built-art{position:absolute;left:0;right:0;top:170px;bottom:0;background:linear-gradient(165deg,rgba(0,0,0,0) 35%,#e07a1c 55%,#c8590f 62%,rgba(0,0,0,0) 72%)}
.audience{position:absolute;top:194px;display:flex;gap:12px;left:209px}
.aud{width:312px;height:80px;text-align:center;padding-top:12px}
.aud h3{font-size:19px;font-weight:500}
.aud p{font-size:9.5px;line-height:1.4;margin-top:6px}
.aud.solo{border:1.5px solid var(--orange);background:var(--sand)}
.aud.team{background:var(--orange);color:var(--white)}

/* how */
.how{height:410px;padding-top:68px}
.steps{position:absolute;top:153px;left:171px;display:flex}
.step{width:238px;height:187px;background:var(--cream);text-align:center;padding-top:38px;position:relative}
.step.dotted{border:1.5px dotted var(--ink);border-top:3px solid var(--ink)}
.step.solid{border:3px solid var(--ink);border-radius:6px;background:var(--white)}
.step h3{font-size:14px;font-weight:700;margin-top:8px}
.step p{font-size:10px;line-height:1.35;margin:4px auto 0;width:200px}
.step .icon{width:54px;height:54px}
.arrow{position:absolute;right:-16px;top:78px;width:30px;height:30px;border-radius:50%;background:var(--orange);z-index:2;display:block}
.arrow svg{display:block;width:30px;height:30px}

/* video */
.video{height:551px;background:radial-gradient(circle at 48% 40%,#fff3c0 0%,#f6b548 22%,#e48a2a 45%,#7a3a10 75%,#1a120a 100%)}
.play{position:absolute;left:487px;top:235px;width:82px;height:82px;border:2px solid var(--white);border-radius:50%;background:rgba(0,0,0,.45);display:block}
.play svg{display:block}

/* testimonials */
.stories{height:370px;background:linear-gradient(180deg,#2c2c2c,#444 60%,#2a2a2a);color:var(--white);text-align:center;padding-top:72px}
.stories h2{font-family:"Playfair Display",serif;font-size:36px}
.stories .score{font-family:"Playfair Display",serif;font-size:16px;margin-top:14px}
.stars{color:var(--gold);letter-spacing:1px}
.stories .lead{font-size:10px;margin-top:10px}
.quotes{display:flex;justify-content:center;gap:52px;margin-top:26px}
.quote{width:194px;font-size:10px;line-height:1.6}
.quote .name{font-family:"Playfair Display",serif;color:var(--gold);margin-top:8px;font-size:12px}
.quote .stars{font-size:15px}
.dots{display:flex;justify-content:center;gap:6px;margin-top:14px}
.dots i{width:4px;height:4px;border-radius:50%;background:#777}
.dots i.on{background:var(--white)}

/* cta */
.cta{height:257px;text-align:center;padding-top:46px}
.cta h2{font-size:41px;font-weight:400;margin-top:8px}
.cta h2 b{font-weight:700}
.cta p{font-size:14.5px;margin-top:10px}
.cta-btn{display:inline-block;margin-top:16px;background:var(--orange);color:var(--white);font-size:13px;font-weight:800;padding:10px 30px;clip-path:polygon(6% 0,100% 0,94% 100%,0 100%)}
footer{height:55px;background:var(--ink);color:var(--white);display:flex;align-items:center;justify-content:center;font-size:13px}
</style>
</head>
<body>
<div class="page">

<section class="hero">
  <div class="hero-art" role="img" aria-label="Sunburst illustration with two caped hero silhouettes standing above a city skyline"></div>
  <div class="hero-city"></div>
  <div class="hero-figures"></div>
  <div class="brand-title">Streak Sparrow</div>
  <svg class="hero-frame" width="420" height="200" viewBox="0 0 420 200">
    <polygon points="0,120 30,0 28,90" fill="#141414"/>
    <polygon points="40,2 418,2 372,198 0,198" fill="none" stroke="#f2b437" stroke-width="1.5"/>
    <polygon points="392,110 372,198 398,170" fill="#141414"/>
  </svg>
  <div class="hero-copy">
    <div class="kicker">REWIRE</div>
    <h1>YOUR <b>DAY</b> FOR<br><b>SUCCESS</b></h1>
    <p>Master the <b>8 Critical</b> Business Habits<br>in <b>90 Days</b>. Statistically <b>proven</b>. <b>Built</b><br>for <b>solo entrepreneurs</b> and teams.</p>
  </div>
  <div class="hero-cta">TRY STREAK SPARROW – $1 TRIAL</div>
</section>

<nav class="nav">
  <div class="brand">Streak Sparrow</div>
  <ul><li>HOME</li><li>8 HABITS</li><li>SOLO &amp; TEAM</li><li>HOW IT WORKS</li><li>TESTIMONIALS</li><li>TRY NOW</li><li>CONTACT</li></ul>
</nav>

<section class="seen">
  <div class="eyebrow">AS</div>
  <h2 class="title"><b>SEEN</b> ON</h2>
  <div class="seen-grid">
    <div class="seen-card"><span class="badge"></span>Ledger Weekly</div>
    <div class="seen-card"><span class="badge"></span>Founder Digest</div>
    <div class="seen-card"><span class="badge"></span>Swift Venture</div>
  </div>
</section>

<section class="habits-head">
  <div class="eyebrow">THE</div>
  <h2 class="title"><b>8 CRITICAL</b> BUSINESS HABITS</h2>
</section>

<section class="habits">
  <div class="habit"><svg viewBox="0 0 76 76" fill="none" stroke="#c8590f" stroke-width="2"><circle cx="50" cy="26" r="16"/><path d="M50 16v10l7 5"/><circle cx="22" cy="22" r="9"/><circle cx="36" cy="56" r="7"/><path d="M24 72c0-8 24-8 24 0"/></svg><h3>Time Discipline</h3><p>Master your schedule and boost productivity.</p></div>
  <div class="habit"><svg viewBox="0 0 76 76" fill="none" stroke="#c8590f" stroke-width="2"><path d="M10 44l30-16v32L10 48z"/><path d="M14 48l4 14h6l-3-12"/><path d="M48 34c6 4 6 16 0 20M56 26c10 8 10 28 0 36"/></svg><h3>Sales Outreach</h3><p>Increase conversions with consistent outreach.</p></div>
  <div class="habit"><svg viewBox="0 0 76 76" fill="none" stroke="#c8590f" stroke-width="2"><circle cx="38" cy="38" r="24"/><circle cx="38" cy="38" r="14"/><path d="M6 14V6h8M62 6h8v8M70 62v8h-8M14 70H6v-8"/></svg><h3>Focus Blocks</h3><p>Deep work periods for real progress.</p></div>
  <div class="habit"><svg viewBox="0 0 76 76" fill="none" stroke="#c8590f" stroke-width="2"><rect x="6" y="10" width="54" height="50" rx="3"/><path d="M6 22h54M16 4v10M30 4v10M44 4v10M14 32h10M30 32h10M14 44h10M30 44h10"/><circle cx="58" cy="58" r="13" fill="#fff"/><path d="M58 50v8h6"/></svg><h3>Weekly Planning</h3><p>Plan ahead and stay on track every week.</p></div>
  <div class="habit"><svg viewBox="0 0 76 76" fill="none" stroke="#c8590f" stroke-width="2"><circle cx="38" cy="20" r="12"/><circle cx="38" cy="20" r="4"/><circle cx="14" cy="54" r="6"/><circle cx="38" cy="50" r="6"/><circle cx="62" cy="54" r="6"/><path d="M4 72c0-8 20-8 20 0M28 70c0-8 20-8 20 0M52 72c0-8 20-8 20 0M38 32v12"/></svg><h3>Lead Management</h3><p>Organize and follow up like a pro.</p></div>
  <div class="habit"><svg viewBox="0 0 76 76" fill="none" stroke="#c8590f" stroke-width="2"><circle cx="18" cy="22" r="7"/><path d="M8 70V36h20v34"/><circle cx="54" cy="18" r="13"/><path d="M48 18l5 5 8-9"/><path d="M40 40h8M40 52h8M40 64h8M54 40h12M54 52h12M54 64h12"/></svg><h3>Accountability</h3><p>Stay motivated with coaching and group support.</p></div>
  <div class="habit"><svg viewBox="0 0 76 76" fill="none" stroke="#c8590f" stroke-width="2"><path d="M10 50l18-18 10 10 26-26"/><path d="M54 16h10v10"/><rect x="30" y="44" width="28" height="24" rx="3"/><circle cx="44" cy="53" r="4"/></svg><h3>Follow-Ups</h3><p>Close more sales and strengthen relationships.</p></div>
  <div class="habit"><svg viewBox="0 0 76 76" fill="none" stroke="#c8590f" stroke-width="2"><path d="M44 6v30M44 8l16 6-16 6"/><circle cx="30" cy="28" r="6"/><path d="M22 72l4-20 8-12 10 8M26 52l-8 20"/><path d="M40 72V54h24v18"/></svg><h3>Leadership Actions</h3><p>Lead your team with intention and clarity.</p></div>
</section>

<section class="built">
  <div class="built-art" role="img" aria-label="Illustration of business people running up a sweeping orange growth arrow"></div>
  <div class="eyebrow">BUILT FOR</div>
  <h2 class="title"><b>DRIVEN INDIVIDUALS</b> &amp;<br>HIGH-PERFORMING <b>TEAMS</b></h2>
  <div class="audience">
    <div class="aud solo"><h3>Solo Users</h3><p>Custom plans, daily nudges, progress streaks, and built-in accountability to help solopreneurs thrive.</p></div>
    <div class="aud team"><h3>Teams &amp; Coaches</h3><p>Dashboards, leaderboards, private feeds, and facilitation tools to build engaged and winning teams.</p></div>
  </div>
</section>

<section class="how">
  <div class="eyebrow">HOW</div>
  <h2 class="title"><b>STREAK SPARROW</b> WORKS</h2>
  <div class="steps">
    <div class="step dotted"><svg class="icon" viewBox="0 0 54 54" fill="none" stroke="#c8590f" stroke-width="2"><path d="M8 6v14M8 6h10v6H8"/><path d="M8 20c20 0 30 4 20 14s-10 14 14 14"/><circle cx="44" cy="42" r="4"/></svg><h3>52-Week Journey</h3><p>Unlock a new habit, lesson, and challenge every week—no guesswork.</p><span class="arrow"><svg viewBox="0 0 30 30"><path d="M13 9l6 6-6 6" fill="none" stroke="#fff" stroke-width="2"/></svg></span></div>
    <div class="step solid"><svg class="icon" viewBox="0 0 54 54" fill="none" stroke="#c8590f" stroke-width="2"><rect x="12" y="18" width="30" height="18" rx="9"/><path d="M20 24v6M17 27h6"/><circle cx="34" cy="27" r="2"/><circle cx="8" cy="8" r="4"/><circle cx="46" cy="8" r="4"/><circle cx="8" cy="46" r="4"/><circle cx="46" cy="46" r="4"/></svg><h3>Gamified System</h3><p>Earn points, track streaks, and celebrate real progress.</p><span class="arrow"><svg viewBox="0 0 30 30"><path d="M13 9l6 6-6 6" fill="none" stroke="#fff" stroke-width="2"/></svg></span></div>
    <div class="step dotted"><svg class="icon" viewBox="0 0 54 54" fill="none" stroke="#c8590f" stroke-width="2"><path d="M6 48h42M10 48V36h10v12M22 48V28h10v20M34 48V20h10v28"/><path d="M36 4v12M36 5l10 4-10 4"/></svg><h3>Adaptive Coaching</h3><p>When engagement drops, Streak Sparrow helps you bounce back.</p></div>
  </div>
</section>

<section class="video" role="img" aria-label="Explainer video poster: caped hero silhouette pushing a boulder against a glowing sunset">
  <span class="play"><svg width="78" height="78" viewBox="0 0 78 78"><path d="M31 25l22 14-22 14z" fill="#fff"/></svg></span>
</section>

<section class="stories" role="region" aria-label="Testimonials">
  <h2>Real Stories, Real Satisfaction</h2>
  <div class="score">Client Feedback: 4.7/5 <span class="stars">★★★★★</span></div>
  <p class="lead">Check out our ratings and reviews to see why our clients trust us for their divorce needs.</p>
  <div class="quotes">
    <div class="quote">Left the military and closed $45K in 44 days using Streak Sparrow.<div class="name">Owen</div><div class="stars">★★★★★</div></div>
    <div class="quote">Finally stayed consistent on lead gen. Changed my entire business.<div class="name">Lyle</div><div class="stars">★★★★★</div></div>
    <div class="quote">Built a million-dollar trucking business while using Streak Sparrow.<div class="name">Dmitri</div><div class="stars">★★★★★</div></div>
  </div>
  <div class="dots"><i></i><i></i><i class="on"></i><i></i><i></i></div>
</section>

<section class="cta">
  <div class="eyebrow">START YOUR</div>
  <h2><b>90-Day Habit</b> Transformation</h2>
  <p>Try Streak Sparrow now for just $1. No fluff. Proven results. Cancel anytime.</p>
  <span class="cta-btn">TRY STREAK SPARROW NOW</span>
</section>

<footer>© 2025 Streak Sparrow. Powered by TopVentureGuide.ca</footer>

</div>
</body>
</html>
```